Voltrix GmbH needs a sensational homepage!

A draft of the performances and the logo were uploaded in the attachment. The homepage should be adapted to the colors of the logo. Either pictures, graphics or icons of the respective topic are to be used for the buttons. Social media Linkedin, Youtube, Instagram should not be missing. An imprint, contact form with telephone number and email address should be given on the home page. The page should definitely be designed to be responsive for all end devices. Texts as well as images and videos are inserted in the sub-menus or pages. Only the structure and a simple application should be given. We have already secured the domain www.voltrix.at.
We are a young, dynamic company with a high technical affinity. Ask for creative suggestions. If something is needed, please contact us.

Target Market(s)

Construction industry, client

Requirements
Must have
• see description
Should not have
• shouldn't be colorful and playful

```html
<!DOCTYPE html>
<html lang="en">
<head>
<meta charset="utf-8">
<title>Voltrix GmbH – Redevelopment &amp; Project Management</title>
<link rel="stylesheet" href="https://fonts.googleapis.com/css2?family=IBM+Plex+Sans:wght@400;500;600&family=IBM+Plex+Serif:wght@500;600;700&display=swap">
<style>
:root{
  --ink:#263a42;
  --ink-deep:#1f2f36;
  --text:#333a3d;
  --muted:#8a8f92;
  --line:#9aa0a3;
  --paper:#ffffff;
  --mist:#ecedee;
  --rule:#e2e4e5;
  --serif:"IBM Plex Serif", Georgia, serif;
  --sans:"IBM Plex Sans", Arial, sans-serif;
}
*{box-sizing:border-box;margin:0;padding:0}
html,body{width:1200px;height:3661px;overflow:hidden;background:var(--paper)}
body{font-family:var(--sans);color:var(--text)}
.page{position:relative;width:1200px;height:3661px;overflow:hidden}
a{color:inherit;text-decoration:none}

/* header */
.site-header{position:absolute;left:0;top:0;width:1200px;height:85px;background:var(--paper)}
.brand{position:absolute;display:flex;align-items:center;gap:10px;font-family:var(--serif);font-weight:500;color:var(--ink);letter-spacing:.18em;white-space:nowrap}
.brand-mark{width:12px;height:12px;background:var(--ink)}
.site-header .brand{left:107px;top:22px;font-size:34px}
.main-nav{position:absolute;top:34px;left:0;font-family:var(--serif);font-size:15px;font-weight:600;color:var(--ink);letter-spacing:.04em}
.main-nav a{position:absolute;white-space:nowrap}
.main-nav .is-active{color:var(--muted);font-weight:500}
.header-phone{position:absolute;left:823px;top:30px;display:flex;align-items:center;gap:10px;font-weight:600;font-size:18px;color:var(--ink);white-space:nowrap}
.social{position:absolute;display:flex}
.social span{display:block;border:1.5px solid var(--ink);border-radius:50%}
.site-header .social{left:1018px;top:28px;gap:9px}
.site-header .social span{width:28px;height:28px}

/* hero */
.hero{position:absolute;left:0;top:85px;width:1200px;height:654px}
.hero-photo{position:absolute;inset:0;background:linear-gradient(100deg,#e5e3de 0%,#dcdad4 35%,#b9bcbd 60%,#8f979c 80%,#d6d8da 100%)}
.hero .brand{left:111px;top:118px;font-size:58px}
.hero-title{position:absolute;left:111px;top:204px;font-family:var(--serif);font-weight:700;font-size:42px;line-height:47px;color:var(--ink);white-space:nowrap}
.hero-text{position:absolute;left:111px;top:313px;width:420px;font-size:18px;line-height:24px;color:#222}
.btn-solid{position:absolute;display:flex;align-items:center;justify-content:center;background:var(--ink);color:#fff;font-weight:600;font-size:15px;letter-spacing:.03em;white-space:nowrap}
.hero .btn-solid{left:111px;top:410px;width:173px;height:47px;border-radius:3px}
.hero-arrows{position:absolute;left:562px;top:580px}

/* section titles */
.framed-title{position:absolute;border:2px solid var(--ink);display:flex;align-items:center;justify-content:center;font-family:var(--serif);font-weight:700;color:var(--ink);letter-spacing:.02em;white-space:nowrap;line-height:1}
.framed-title::after{content:"";position:absolute;inset:5px;border:1.5px solid var(--line)}

/* services */
.services-title{left:436px;top:812px;width:325px;height:77px;font-size:39px}
.service-card-frame{position:absolute;left:144px;top:968px;width:324px;height:442px;border:2px solid var(--ink)}
.service-card-frame::after{content:"";position:absolute;inset:6px;border:2px solid var(--line)}
.service{position:absolute;width:250px;text-align:center}
.service-icon{width:100px;height:100px;margin:0 auto;border-radius:6px;background:linear-gradient(160deg,#e6e8e9,#cfd3d5)}
.service h3{font-family:var(--serif);font-weight:500;font-size:19px;line-height:24px;color:#1e1e1e;margin-top:32px}
.service p{font-size:14.4px;line-height:20.8px;color:#3b3b3b;margin-top:14px}
.btn-outline{position:absolute;width:155px;height:43px;border:2px solid var(--line);display:flex;align-items:center;justify-content:center;font-weight:600;font-size:15px;color:var(--ink)}

/* banner */
.banner{position:absolute;left:0;top:1504px;width:1200px;height:407px;background:linear-gradient(90deg,#eeeff0 0%,#e6e7e8 50%,#d4d6d8 75%,#e2e3e4 100%)}
.banner-text{position:absolute;left:0;top:122px;width:1200px;text-align:center;font-family:var(--serif);font-weight:500;font-size:30px;line-height:44px;color:var(--ink)}
.banner .btn-solid{left:502px;top:233px;width:195px;height:52px}

/* about */
.about-title{left:144px;top:2008px;height:78px;padding:0 22px;font-size:35px}
.about-text{position:absolute;left:144px;top:2120px;width:390px;font-size:16.6px;line-height:22.5px;color:#333}
.about .btn-solid{left:146px;top:2332px;width:197px;height:51px}
.about-media{position:absolute;left:604px;top:1911px;width:596px;height:574px;background:linear-gradient(135deg,#6d7478 0%,#3d4549 45%,#252c30 100%)}
.play{position:absolute;left:269px;top:239px}

/* map */
.map{position:absolute;left:0;top:2485px;width:1200px;height:508px;background:linear-gradient(120deg,#b9b9b9,#a9a9a9 50%,#c2c2c2)}
.map-card{position:absolute;left:499px;top:70px;width:269px;height:171px;background:#fff;border-radius:10px;text-align:center}
.map-card::after{content:"";position:absolute;left:105px;bottom:-30px;border-right:30px solid transparent;border-top:32px solid #fff}
.map-card .brand{left:50%;transform:translateX(-50%);top:28px;font-size:36px}
.map-card p{position:absolute;left:0;top:101px;width:100%;font-size:16px;line-height:22px;color:#333}

/* contact */
.contact-title{left:144px;top:3081px;height:78px;padding:0 24px;font-size:37px}
.contact-item{position:absolute;left:144px;display:flex;gap:20px;font-size:16px;line-height:21px;color:#333}
.contact-item svg{flex:none}
.form-field{position:absolute;width:252px;border-bottom:1.5px solid #9a9a9a;height:40px;font-size:13.5px;color:#555}
.form-field.wide{width:517px;height:48px}
.submit{position:absolute;left:537px;top:3335px;width:153px;height:43px;background:var(--ink);color:#fff;font-family:var(--serif);font-weight:600;font-size:14px;letter-spacing:.05em;display:flex;align-items:center;justify-content:center}

/* footer */
.site-footer{position:absolute;left:0;top:3483px;width:1200px;height:178px;border-top:1px solid var(--rule)}
.site-footer .social{left:558px;top:49px;gap:12px}
.site-footer .social span{width:36px;height:36px}
.copyright{position:absolute;left:0;top:110px;width:1200px;text-align:center;font-size:15.5px;color:#333}
</style>
</head>
<body>
<div class="page">

  <header class="site-header">
    <a class="brand" href="#"><span class="brand-mark"></span>VOLTRIX</a>
    <nav class="main-nav">
      <a class="is-active" style="left:432px" href="#">HOME</a>
      <a style="left:515px" href="#">ABOUT</a>
      <a style="left:606px" href="#">SERVICES</a>
      <a style="left:718px" href="#">CONTACT</a>
    </nav>
    <div class="header-phone">
      <svg width="20" height="20" viewBox="0 0 24 24" aria-hidden="true"><path fill="#7b8387" d="M6.6 10.8a15 15 0 0 0 6.6 6.6l2.2-2.2a1 1 0 0 1 1-.25 11.4 11.4 0 0 0 3.6.57 1 1 0 0 1 1 1V20a1 1 0 0 1-1 1A17 17 0 0 1 3 4a1 1 0 0 1 1-1h3.5a1 1 0 0 1 1 1c0 1.25.2 2.45.57 3.57a1 1 0 0 1-.25 1z"/></svg>
      555 0140 7700
    </div>
    <div class="social" aria-label="Social media links"><span></span><span></span><span></span></div>
  </header>

  <section class="hero">
    <div class="hero-photo" role="img" aria-label="Photo from above of a business team meeting around a glass table with charts, on a light tiled floor"></div>
    <div class="brand"><span class="brand-mark"></span>VOLTRIX</div>
    <h1 class="hero-title">Redevelopment<br>Project management</h1>
    <p class="hero-text">Sed ut perspiciatis unde omnis iste natus sit voluptatem accusantium doloremque laudtium, totam rem aperiam, eaque ipsa</p>
    <a class="btn-solid" href="#">LEARN MORE</a>
    <svg class="hero-arrows" width="74" height="20" viewBox="0 0 74 20" aria-hidden="true"><path d="M2 10h28M2 10l7-6M2 10l7 6M44 10h28M72 10l-7-6M72 10l-7 6" stroke="#fff" stroke-width="2" fill="none"/></svg>
  </section>

  <section class="services">
    <h2 class="framed-title services-title">OUR SERVICE</h2>
    <div class="service-card-frame"></div>

    <div class="service" style="left:180px;top:1002px">
      <div class="service-icon" role="img" aria-label="Scaffolding icon"></div>
      <h3>Scaffolding</h3>
      <p>Sed ut perspiciatis unde omnis iste natus sit voluptatem accusantium doloremque laudantium, totam rem aperiam, eaque ipsa quae ab illo inentore veritatis et quasi architecto beatae vitae dicta sunt explicabo.Sed ut perspiciatis unde omnis iste natus sit voluptatem accusantium dolomque laudantium, totam rem aperiam, eaque ipsa quae ab illo inentore</p>
    </div>

    <div class="service" style="left:511px;top:1002px">
      <div class="service-icon" role="img" aria-label="Gear and light bulb icon"></div>
      <h3>Redevelopment<br>Project management</h3>
      <p>Sed ut perspiciatis unde omnis iste natus sit voluptatem accusantium doloremque laudantium, totam rem aperiam, eaque ipsa quae ab illo inentore veritatis et quasi architecto beatae vitae dicta sunt explicabo.</p>
    </div>
    <a class="btn-outline" style="left:557px;top:1345px" href="#">Learn More</a>

    <div class="service" style="left:813px;top:1002px">
      <div class="service-icon" role="img" aria-label="Team and handshake icon"></div>
      <h3>Screed &amp; insulation</h3>
      <p>Sed ut perspiciatis unde omnis iste natus sit voluptatem accusantium doloremque laudantium, totam rem aperiam, eaque ipsa quae ab illo inentore veritatis et quasi architecto beatae vitae dicta sunt explicabo. laudantium, totam rem</p>
    </div>
    <a class="btn-outline" style="left:860px;top:1345px" href="#">Learn More</a>
  </section>

  <section class="banner" role="img" aria-label="Faded photo of a man working at a desk in an office">
    <p class="banner-text">Nemo enim ipsam voluptatem quia voluptas<br>sit aspernatur aut odit aut fugit</p>
    <a class="btn-solid" href="#">LEARN MORE</a>
  </section>

  <section class="about">
    <h2 class="framed-title about-title">ABOUT VOLTRIX</h2>
    <p class="about-text">Sed ut perspiciatis unde omnis iste natus error sit voluptatem accusantium doloremque laudantium, totam rem aperiam, eaque ipsa quae ab illo inventore veritatis et quasi architecto beatae vitae dicta sunt explicabo. Nemo enim ipsam voluptatem quia voluptas sit aspernatur aut odit aut fugit, sed quia consequuntur magni dolores eos qui ratione voluptatem sequi nesciunt.</p>
    <a class="btn-solid" href="#">LEARN MORE</a>
    <div class="about-media" role="img" aria-label="Video still of two colleagues working together at a laptop">
      <svg class="play" width="58" height="58" viewBox="0 0 58 58" aria-label="Play video"><circle cx="29" cy="29" r="28" fill="#fff"/><path d="M23 17l18 12-18 12z" fill="#3a4246"/></svg>
    </div>
  </section>

  <section class="map" role="img" aria-label="Greyscale regional road map showing the office location">
    <div class="map-card">
      <div class="brand"><span class="brand-mark"></span>VOLTRIX</div>
      <p>#262 enim ipsam vatem<br>quia voluptas</p>
    </div>
  </section>

  <section class="contact">
    <h2 class="framed-title contact-title">CONTACT US</h2>
    <div class="contact-item" style="top:3190px">
      <svg width="40" height="40" viewBox="0 0 40 40" aria-hidden="true"><circle cx="20" cy="20" r="18.5" fill="none" stroke="#7b8387" stroke-width="1.5"/><path d="M20 11a6 6 0 0 0-6 6c0 4.5 6 11 6 11s6-6.5 6-11a6 6 0 0 0-6-6z" fill="none" stroke="#7b8387" stroke-width="1.6"/><circle cx="20" cy="17" r="2" fill="#7b8387"/></svg>
      <div>Voltrix<br>#262 enim ipsam vatem<br>quia voluptas</div>
    </div>
    <div class="contact-item" style="top:3270px">
      <svg width="40" height="40" viewBox="0 0 40 40" aria-hidden="true"><circle cx="20" cy="20" r="18.5" fill="none" stroke="#7b8387" stroke-width="1.5"/><path fill="#7b8387" d="M15.5 18.5a11 11 0 0 0 5 5l1.7-1.7a.8.8 0 0 1 .8-.2 8.5 8.5 0 0 0 2.7.4.8.8 0 0 1 .8.8v2.6a.8.8 0 0 1-.8.8A12.8 12.8 0 0 1 13 13.8a.8.8 0 0 1 .8-.8h2.6a.8.8 0 0 1 .8.8c0 .95.15 1.85.43 2.7a.8.8 0 0 1-.2.8z"/></svg>
      <div>Phone:<br>555 0140 7762</div>
    </div>
    <div class="contact-item" style="top:3327px">
      <svg width="40" height="40" viewBox="0 0 40 40" aria-hidden="true"><circle cx="20" cy="20" r="18.5" fill="none" stroke="#7b8387" stroke-width="1.5"/><rect x="12" y="14" width="16" height="12" rx="1.5" fill="#7b8387"/><path d="M12.5 15l7.5 6 7.5-6" fill="none" stroke="#fff" stroke-width="1.4"/></svg>
      <div>Email:<br>info@voltrix.at</div>
    </div>

    <form>
      <label class="form-field" style="left:537px;top:3092px">First name</label>
      <label class="form-field" style="left:801px;top:3092px">Last Name</label>
      <label class="form-field" style="left:537px;top:3180px">Email</label>
      <label class="form-field" style="left:801px;top:3180px">Phone Number</label>
      <label class="form-field wide" style="left:537px;top:3252px">Message</label>
      <div class="submit">SUBMIT</div>
    </form>
  </section>

  <footer class="site-footer">
    <div class="social" aria-label="Social media links"><span></span><span></span><span></span></div>
    <p class="copyright">Voltrix © 2021 All Rights Reserved | Privacy Policy | Imprint</p>
  </footer>

</div>
</body>
</html>
```